Flyer-Design für betriebliche Gesundheitsvorsorge
Zielgruppe
'Werk im Schwung' soll Unternehmen die Möglichkeit bieten unsere Dienste im Sinne der Gesundheitsvorsorge für ihre Mitarbeiter in Anspruch zu nehmen. Dies beinhaltet Massagen am Arbeitsplatz (in separaten Räumlichkeiten), Arbeitsplatzberatung bezgl. Ergonomie, Workshops zu kurzen Übungen die in den Arbeitsalltag integriert werden können, Verdeutlichung der Eigenverantwortung für einen gesunden Körper, ....
Aufgabenstellung
Die Werbekarte sollte in DIN Lang format sein.

```html
<!DOCTYPE html>
<html lang="de">
<head>
<meta charset="utf-8">
<title>Werk im Schwung – DIN Lang Flyer</title>
<link rel="stylesheet" href="https://fonts.googleapis.com/css2?family=Open+Sans:wght@400;600;700;800&display=swap">
<style>
  :root {
    --teal: #7dbdb2;
    --teal-dark: #5fa89c;
    --ink: #454545;
    --ink-soft: #6a6a6a;
    --paper: #ffffff;
    --stage: #e9e9e9;
    --rule: #9a9a9a;
  }
  * { box-sizing: border-box; margin: 0; padding: 0; }
  html, body { width: 1200px; height: 1200px; overflow: hidden; }
  body {
    background: var(--stage);
    font-family: "Open Sans", Arial, sans-serif;
    color: var(--ink);
    display: flex;
    flex-direction: column;
    align-items: center;
    justify-content: center;
    gap: 40px;
  }
  .card {
    position: relative;
    width: 1040px;
    height: 495px;
    background: var(--paper);
    box-shadow: 0 6px 18px rgba(0,0,0,.18);
    overflow: hidden;
  }
  .band {
    position: absolute;
    left: 0; right: 0; bottom: 0;
    height: 92px;
    background: var(--teal);
    color: #fff;
    display: flex;
    align-items: center;
  }
  /* brand block */
  .brand {
    position: absolute;
    display: flex;
    align-items: center;
    gap: 16px;
  }
  .brand-dot {
    width: 64px; height: 64px;
    border-radius: 50%;
    background: var(--teal);
    flex: none;
  }
  .brand-text { border-left: 1px solid var(--rule); padding-left: 16px; }
  .brand-name {
    font-size: 38px;
    font-weight: 700;
    color: var(--teal);
    line-height: 1.05;
  }
  .brand-claim {
    font-size: 14px;
    color: var(--ink-soft);
    letter-spacing: .4px;
    margin-top: 6px;
  }
  /* front side */
  .front .brand { left: 40px; top: 40px; }
  .contact {
    position: absolute;
    right: 40px; top: 38px;
    text-align: right;
    font-size: 15px;
    color: var(--ink);
    line-height: 1.5;
  }
  .contact .web { font-size: 22px; font-weight: 700; margin-bottom: 12px; }
  .services {
    position: absolute;
    left: 40px; right: 40px; top: 158px;
    font-size: 19px;
    line-height: 1.45;
    color: var(--ink);
  }
  .services .sep { color: var(--teal); }
  .photo-row {
    position: absolute;
    left: 40px; right: 40px; top: 240px;
    height: 165px;
    display: flex;
    gap: 10px;
  }
  .photo {
    flex: 1;
    background: linear-gradient(160deg, #c9d3dc, #8f99a3);
  }
  .photo.office { background: linear-gradient(160deg, #eef0f2, #a7adb4); }
  .photo.site { background: linear-gradient(160deg, #b9c4cc, #6d6a63); }
  .photo.desk { background: linear-gradient(160deg, #f1f3f5, #8e9ab2); }
  .front .band { padding-left: 40px; font-size: 26px; font-weight: 700; }

  /* back side */
  .back .brand { left: 40px; top: 30px; z-index: 2; }
  .hero {
    position: absolute;
    left: 40px; top: 128px;
    width: 530px; height: 275px;
    background: linear-gradient(180deg, #f4f4f4 0%, #dcdcdc 70%, #bcbcbc 100%);
  }
  .pitch {
    position: absolute;
    left: 610px; right: 40px; top: 64px;
  }
  .pitch h2 {
    font-size: 25px;
    font-weight: 700;
    color: var(--teal);
    line-height: 1.3;
    margin-bottom: 18px;
  }
  .benefits { list-style: none; }
  .benefits li {
    display: flex;
    gap: 10px;
    font-size: 16px;
    line-height: 1.35;
    color: var(--ink);
    margin-bottom: 9px;
  }
  .benefits svg { flex: none; margin-top: 3px; }
  .back .band {
    justify-content: flex-end;
    padding-right: 40px;
    font-size: 29px;
    letter-spacing: 1px;
    font-weight: 400;
  }
  .back .band b { font-weight: 800; }
</style>
</head>
<body>

  <section class="card front">
    <div class="brand">
      <div class="brand-dot"></div>
      <div class="brand-text">
        <div class="brand-name">Werk im Schwung</div>
        <div class="brand-claim">Gesundheitsvorsorge am Arbeitsplatz</div>
      </div>
    </div>
    <div class="contact">
      <div class="web">www.werkimschwung.at</div>
      <div>+43 (0) 660 482 3917</div>
      <div>hallo@werkimschwung.at</div>
    </div>
    <p class="services">
      Präventive Intervention bei haltungsbedingten Schmerzen <span class="sep">//</span> Heilmassage <span class="sep">//</span> Sportmassage<br>
      Bindegewebsmassage <span class="sep">//</span> Schröpfen <span class="sep">//</span> Aromatherapie <span class="sep">//</span> Kinesio Taping
    </p>
    <div class="photo-row">
      <div class="photo" role="img" aria-label="Foto: Mann am Bildschirm mit Nackenschmerzen"></div>
      <div class="photo office" role="img" aria-label="Foto: Frau am Schreibtisch mit Rückenschmerzen"></div>
      <div class="photo site" role="img" aria-label="Foto: Bauarbeiter vor Baustelle hält sich den Rücken"></div>
      <div class="photo desk" role="img" aria-label="Foto: Person auf Bürostuhl mit Kreuzschmerzen"></div>
    </div>
    <div class="band">Werk im Schwung – Gesundheitsvorsorge an Ihrem Arbeitsplatz</div>
  </section>

  <section class="card back">
    <div class="brand">
      <div class="brand-dot"></div>
      <div class="brand-text">
        <div class="brand-name">Werk im Schwung</div>
        <div class="brand-claim">Gesundheitsvorsorge am Arbeitsplatz</div>
      </div>
    </div>
    <div class="hero" role="img" aria-label="Foto: Masseurin mit Massageliege vor weißem Firmenauto"></div>
    <div class="pitch">
      <h2>Lassen Sie sich von Gesundheit am Arbeitsplatz überzeugen!</h2>
      <ul class="benefits">
        <li><svg width="14" height="14" viewBox="0 0 14 14"><path d="M1.5 7.5 L5.5 11.5 L12.5 2.5" fill="none" stroke="#7dbdb2" stroke-width="2.4" stroke-linecap="round" stroke-linejoin="round"/></svg>Direkt an Ihrem Arbeitsplatz</li>
        <li><svg width="14" height="14" viewBox="0 0 14 14"><path d="M1.5 7.5 L5.5 11.5 L12.5 2.5" fill="none" stroke="#7dbdb2" stroke-width="2.4" stroke-linecap="round" stroke-linejoin="round"/></svg>Keine weiten Umwege für Sie</li>
        <li><svg width="14" height="14" viewBox="0 0 14 14"><path d="M1.5 7.5 L5.5 11.5 L12.5 2.5" fill="none" stroke="#7dbdb2" stroke-width="2.4" stroke-linecap="round" stroke-linejoin="round"/></svg><span>Während Ihrer Arbeitszeit können Sie sich angenehm behandeln lassen</span></li>
        <li><svg width="14" height="14" viewBox="0 0 14 14"><path d="M1.5 7.5 L5.5 11.5 L12.5 2.5" fill="none" stroke="#7dbdb2" stroke-width="2.4" stroke-linecap="round" stroke-linejoin="round"/></svg><span>Behandlungen werden individuell an Ihre Bedürfnisse angepasst</span></li>
        <li><svg width="14" height="14" viewBox="0 0 14 14"><path d="M1.5 7.5 L5.5 11.5 L12.5 2.5" fill="none" stroke="#7dbdb2" stroke-width="2.4" stroke-linecap="round" stroke-linejoin="round"/></svg><span>Unser Team bildet sich ständig weiter, um den besten Service in jeder Situation für Sie zu erreichen</span></li>
      </ul>
    </div>
    <div class="band"><span><b>HEALTHY</b> BODY // <b>HEALTHY</b> MIND // <b>HEALTHY</b> SOUL</span></div>
  </section>

</body>
</html>
```